Introduction brochure for IT Company

We need a brochure for introducing our new small business services to the market.

We need a template that we can alter and play with as services change, and was thinking about the following:

A front page which has logo (attached), and follows colour scheme used on our website www.quillotech.com.au, that has a small description of the service/or us, we are introducing and Call us on 1300 627 398 at the bottom of page.
For the first print only front page and back page will be used, as we are still refining the service. We will be introducing the company to new prospects face to face and want to leave them with a small brochure which explains what we do for them, and clear contact details.

Middle section we have not worked out fully yet, as it depends on space available, but please use points under service on our website for now to fill in with some points.

Last page we want to have the last 1/3 of page to be our contact details along with a google map of our location etc. like the contact us page on website.

We prefer to stay on the lighter side, so more playful in style but you guys are the experts.

Target Market(s)

Small business 1-10 Employees

Industry/Entity Type

It Company

Font styles to use
Serif

Requirements
Must have
• Clear contact details, playful design which is easy to read. Follow colour scheme or close to website, www.quillotech.com.au, as this is reflected in all our marketing. Some artistic license is of course given.
Nice to have
• Nothing comes to mind, go crazy and make it fun.
Should not have
• typical images of large scale server racks and enterprise level images. Stay small business.

```html
<!DOCTYPE html>
<html lang="en">
<head>
<meta charset="utf-8">
<title>Quillo Tech – About Us &amp; Services</title>
<link href="https://fonts.googleapis.com/css2?family=Open+Sans:ital,wght@0,400;0,600;0,700;0,800;1,400;1,600&display=swap" rel="stylesheet">
<style>
  :root {
    --red: #d1232a;
    --red-dark: #a9151c;
    --ink: #2b2b2b;
    --text: #444;
    --paper: #ffffff;
    --page-shade: #eef0f4;
    --backdrop: #e4e5e8;
    --hex: #111;
  }
  * { box-sizing: border-box; margin: 0; padding: 0; }
  html, body {
    width: 1200px; height: 789px; overflow: hidden;
    background: var(--backdrop);
    font-family: "Open Sans", Arial, sans-serif;
    color: var(--text);
  }
  .spread {
    position: absolute; left: 30px; top: 18px;
    width: 1140px; height: 753px;
    display: flex;
    box-shadow: 0 6px 24px rgba(0,0,0,.18);
  }
  .page {
    position: relative; width: 570px; height: 100%;
    background: var(--paper);
    overflow: hidden;
    border-top: 6px solid var(--red);
  }
  .page--left {
    background: linear-gradient(to right, var(--paper) 88%, var(--page-shade));
    display: flex; flex-direction: column;
    padding: 58px 0 60px;
  }
  .page--right { background: linear-gradient(to left, var(--paper) 88%, var(--page-shade)); }

  .section-tab {
    position: absolute; top: 0; left: 40px;
    background: var(--red); color: #fff;
    font-weight: 700; font-size: 17px; letter-spacing: 1px;
    padding: 8px 28px 9px;
    text-transform: uppercase;
  }

  /* About us */
  .about-copy {
    padding: 0 40px 0 44px;
    font-size: 10.3px; line-height: 1.44;
  }
  .about-copy p { margin-bottom: 6px; }
  .help-heading {
    margin: 12px 30px 0 44px;
    color: var(--red); font-weight: 700; font-size: 15.5px;
    text-transform: uppercase; letter-spacing: .3px;
  }
  .options {
    list-style: none;
    margin: 12px 40px 0;
    display: flex; justify-content: space-between;
  }
  .option { width: 112px; text-align: center; }
  .option__art {
    width: 92px; height: 62px; margin: 0 auto;
    border-radius: 6px;
    background: linear-gradient(160deg, #cfe0f3, #7c9cc2 70%, #9aa3ad);
  }
  .option__rule { display: block; margin: 8px auto 6px; }
  .option__label { font-size: 10.5px; line-height: 1.3; color: var(--ink); font-weight: 600; }
  .call-band {
    margin-top: auto;
    background: var(--red); color: #fff;
    font-weight: 700; font-size: 25px; letter-spacing: 1.5px;
    padding: 14px 44px;
  }

  /* Services */
  .page--right .section-tab { left: 30px; }
  .services-intro {
    position: absolute; top: 58px; left: 32px; right: 30px;
    color: var(--red); font-weight: 700; font-size: 12.5px;
  }
  .service-list {
    position: absolute; top: 88px; left: 30px; right: 30px;
    list-style: none;
  }
  .service {
    display: flex; align-items: center; gap: 14px;
    margin-bottom: 10px;
  }
  .service--flip { flex-direction: row-reverse; }
  .service__icon { flex: 0 0 56px; }
  .service__title { color: var(--red); font-weight: 700; font-size: 11.5px; margin-bottom: 2px; }
  .service__text { font-size: 9.4px; line-height: 1.4; color: var(--text); }
  .closing-note {
    position: absolute; left: 32px; right: 34px; bottom: 48px;
    color: var(--red); font-style: italic; font-size: 12px; line-height: 1.5;
  }
</style>
</head>
<body>
<main class="spread">

  <section class="page page--left">
    <h2 class="section-tab">About us</h2>
    <div class="about-copy">
      <p>Quillo Tech is a reliable one-stop service for all things tech and web. Specialising in computer services, IT support services and internet installation, Quillo Tech's services are available around the Greater Riverton area.</p>
      <p>Quillo Tech began full time operations in August 2015, after functioning as a part time sole trader since 2010. From his years as an IT Manager for a major telecommunications network and several technology companies around Australia, the company's director and founder, Daniel Marsh, noticed a major lack of effective computer and IT services.</p>
      <p>Daniel decided to capitalise on his 19 years of experience and establish Quillo Tech, which unlike bigger companies out there, focuses on proactive solutions that take into account the bigger picture and pre-empts customers' needs and habits. The result is a service that is all-encompassing, easy and quick to deal with, giving customers everything they require upfront.</p>
      <p>Since Quillo Tech went full time, demand for affordable computer and IT services, and internet installation has escalated. Customers have discovered that IT support can tick all the boxes for cost-effectiveness, reliability, fast turnaround and above all, making computers and technology easy to understand.</p>
      <p>Quillo Tech's ability to deliver cutting edge IT support and solutions with a difference has challenged the marketplace and helped customers realise what value they should be getting for their money. The company invests time to research each job in regards to the customer's needs in order to provide a solution that is well within budget.</p>
      <p>From stay-at-home mum and dads managing a household where the kids' online hobbies require more bandwidth, to small companies that need an effective IT support service, Quillo Tech meets needs easily.</p>
      <p>Talk to us today about what you need and get a quote, no strings attached.</p>
    </div>

    <h3 class="help-heading">Need some help? We offer several options.</h3>

    <ul class="options">
      <li class="option">
        <div class="option__art" role="img" aria-label="Illustration of a house with a laptop computer"></div>
        <svg class="option__rule" width="100" height="8" viewBox="0 0 100 8"><path d="M0 1H44L50 7L56 1H100" fill="none" stroke="#d1232a" stroke-width="1"/></svg>
        <p class="option__label">Residential computer / network issues</p>
      </li>
      <li class="option">
        <div class="option__art" role="img" aria-label="Illustration of office computers linked to a cloud"></div>
        <svg class="option__rule" width="100" height="8" viewBox="0 0 100 8"><path d="M0 1H44L50 7L56 1H100" fill="none" stroke="#d1232a" stroke-width="1"/></svg>
        <p class="option__label">Business computer / network issues</p>
      </li>
      <li class="option">
        <div class="option__art" role="img" aria-label="Illustration of a small house with a network cable"></div>
        <svg class="option__rule" width="100" height="8" viewBox="0 0 100 8"><path d="M0 1H44L50 7L56 1H100" fill="none" stroke="#d1232a" stroke-width="1"/></svg>
        <p class="option__label">Home Networking</p>
      </li>
      <li class="option">
        <div class="option__art" role="img" aria-label="Illustration of a new house with a globe and network plug"></div>
        <svg class="option__rule" width="100" height="8" viewBox="0 0 100 8"><path d="M0 1H44L50 7L56 1H100" fill="none" stroke="#d1232a" stroke-width="1"/></svg>
        <p class="option__label">New Home networking</p>
      </li>
    </ul>

    <p class="call-band">CALL US ON : 1300 627 398</p>
  </section>

  <section class="page page--right">
    <h2 class="section-tab">Services</h2>
    <p class="services-intro">Quillo Tech provide a wide range of services to home and office users.</p>

    <ul class="service-list">
      <li class="service">
        <svg class="service__icon" width="56" height="56" viewBox="0 0 56 56" aria-hidden="true">
          <polygon points="16,2 40,2 54,16 54,40 40,54 16,54 2,40 2,16" fill="#111"/>
          <rect x="15" y="17" width="26" height="17" rx="1.5" fill="none" stroke="#d1232a" stroke-width="3"/>
          <rect x="24" y="35" width="8" height="4" fill="#d1232a"/><rect x="19" y="39" width="18" height="3" fill="#d1232a"/>
        </svg>
        <div>
          <h4 class="service__title">Computer hardware and software installations and troubleshooting</h4>
          <p class="service__text">Whatever computer problems you're experiencing, whether hardware or software related, we can fix it. Our highly skilled technicians specialise in all types of hardware and software installations, and make configurations to suit your needs.</p>
        </div>
      </li>
      <li class="service service--flip">
        <svg class="service__icon" width="56" height="56" viewBox="0 0 56 56" aria-hidden="true">
          <polygon points="16,2 40,2 54,16 54,40 40,54 16,54 2,40 2,16" fill="#111"/>
          <rect x="19" y="13" width="18" height="30" rx="2" fill="#d1232a"/>
          <rect x="22" y="17" width="12" height="3" fill="#111"/><circle cx="28" cy="34" r="3" fill="#111"/>
        </svg>
        <div>
          <h4 class="service__title">Custom built computer service</h4>
          <p class="service__text">Anywhere in the region, our consultants and technicians will help you choose a system that is perfect for your usage. Often people spend more money than they need to because a salesperson has pointed them in the wrong direction. At Quillo Tech, our computer service stands out because we pride ourselves on getting to know our customers' needs and building solutions to suit them.</p>
        </div>
      </li>
      <li class="service">
        <svg class="service__icon" width="56" height="56" viewBox="0 0 56 56" aria-hidden="true">
          <polygon points="16,2 40,2 54,16 54,40 40,54 16,54 2,40 2,16" fill="#111"/>
          <path d="M13 25a21 21 0 0 1 30 0M18 30a14 14 0 0 1 20 0M23 35a7 7 0 0 1 10 0" fill="none" stroke="#d1232a" stroke-width="3" stroke-linecap="round"/>
          <circle cx="28" cy="40" r="2.6" fill="#d1232a"/>
        </svg>
        <div>
          <h4 class="service__title">Internet installations and advice</h4>
          <p class="service__text">We can advise you on which broadband plan would suit your usage, to make sure you are not paying too much for your internet service. Our internet installation is a straightforward process - we will set it all up for you, so you don't have to worry about anything except getting online and doing what you need to. Easy!</p>
        </div>
      </li>
      <li class="service service--flip">
        <svg class="service__icon" width="56" height="56" viewBox="0 0 56 56" aria-hidden="true">
          <polygon points="16,2 40,2 54,16 54,40 40,54 16,54 2,40 2,16" fill="#111"/>
          <rect x="12" y="24" width="32" height="10" rx="2" fill="#d1232a"/>
          <path d="M17 24l4-7h14l4 7" fill="none" stroke="#d1232a" stroke-width="3"/>
          <circle cx="19" cy="36" r="3.5" fill="#d1232a"/><circle cx="37" cy="36" r="3.5" fill="#d1232a"/>
        </svg>
        <div>
          <h4 class="service__title">Wired and wireless network installations and advice</h4>
          <p class="service__text">We can get your new home or business network functioning better and faster by optimising the way things are connected and performing an internal clean up on your computer. Whether wired or wireless, our network installation is quick and effective.</p>
        </div>
      </li>
      <li class="service">
        <svg class="service__icon" width="56" height="56" viewBox="0 0 56 56" aria-hidden="true">
          <polygon points="16,2 40,2 54,16 54,40 40,54 16,54 2,40 2,16" fill="#111"/>
          <ellipse cx="26" cy="17" rx="11" ry="4" fill="#d1232a"/>
          <path d="M15 21v6c0 2 5 4 11 4s11-2 11-4v-6c0 2-5 4-11 4s-11-2-11-4zM15 30v6c0 2 5 4 11 4s11-2 11-4v-6c0 2-5 4-11 4s-11-2-11-4z" fill="#d1232a"/>
          <circle cx="38" cy="38" r="6" fill="none" stroke="#d1232a" stroke-width="2.5"/>
        </svg>
        <div>
          <h4 class="service__title">Data backup and recovery</h4>
          <p class="service__text">Never lose data again! We have backup solutions to suit any home or business requirement. Our solutions will ensure that your vital information will still be safe, should the worst happen.</p>
        </div>
      </li>
      <li class="service service--flip">
        <svg class="service__icon" width="56" height="56" viewBox="0 0 56 56" aria-hidden="true">
          <polygon points="16,2 40,2 54,16 54,40 40,54 16,54 2,40 2,16" fill="#111"/>
          <path d="M28 12l13 5v9c0 9-6 15-13 18c-7-3-13-9-13-18v-9z" fill="#d1232a"/>
          <path d="M22 28l5 5l8-9" fill="none" stroke="#111" stroke-width="3"/>
        </svg>
        <div>
          <h4 class="service__title">Computer and network IT security services</h4>
          <p class="service__text">60% of computers in Australia today do not have adequate security. We have solutions for any type of computer or network to make sure your system is protected at all times from the malware and viruses. IT security services are completely essential - ask us more.</p>
        </div>
      </li>
      <li class="service">
        <svg class="service__icon" width="56" height="56" viewBox="0 0 56 56" aria-hidden="true">
          <polygon points="16,2 40,2 54,16 54,40 40,54 16,54 2,40 2,16" fill="#111"/>
          <circle cx="20" cy="19" r="4" fill="#d1232a"/>
          <path d="M14 40v-11c0-3 2-5 6-5s6 2 6 5v11z" fill="#d1232a"/>
          <path d="M28 38h14M32 38l6-12" fill="none" stroke="#d1232a" stroke-width="3"/>
        </svg>
        <div>
          <h4 class="service__title">IT training</h4>
          <p class="service__text">We can help you learn about your computer hardware or software. We also offer training on any new purchase you make for your computer, from your monitor to your HD video cam.</p>
        </div>
      </li>
    </ul>

    <p class="closing-note">We have partnered with some of the best vendors and suppliers in the industry to be able to provide you with the best hardware and software on the market today. So do yourself a favour, call us today and get the help you have always wanted.</p>
  </section>

</main>
</body>
</html>
```